Recruitment Agency in Texas, needs a stand out header letter

Our colours are red and grey and can be found on our website
just my logo will be sufficient and address...

Target Market(s)

Engineering Manufacturing

Colors
0094D4
00A9DD
6FCCEA
C7EBF8
E9F6FB
EB3D1F
EC4F4E
F09395
F8D3D4
FCEDEE

Requirements
Must have
• use colors red and grey
Should not have
• Please use same colors and font as my logo. My website is kelbrinstaffing.com

```html
<!DOCTYPE html>
<html lang="en">
<head>
<meta charset="utf-8">
<title>KelbrinStaffing Letterhead</title>
<link href="https://fonts.googleapis.com/css2?family=Roboto:wght@300;400;500&family=Pinyon+Script&display=swap" rel="stylesheet">
<style>
  :root {
    --brand-red: #e31e24;
    --brand-grey: #5f5f62;
    --ink: #2b2b2b;
    --ink-soft: #6a6a6a;
    --paper: #f6f6f6;
    --backdrop: #e2e2e2;
    --rule: #9a9a9a;
    --ghost: #ebebeb;
  }
  * { box-sizing: border-box; margin: 0; padding: 0; }
  html, body { width: 1200px; height: 1200px; overflow: hidden; }
  body {
    background: var(--backdrop);
    font-family: "Roboto", Arial, sans-serif;
    font-weight: 300;
    color: var(--ink);
  }
  .letterhead {
    position: absolute;
    left: 204px; top: 40px;
    width: 792px; height: 1120px;
    background: var(--paper);
    box-shadow: 0 6px 24px rgba(0,0,0,0.12);
    overflow: hidden;
  }
  .accent-bar {
    position: absolute; left: 44px; top: 0;
    width: 255px; height: 8px;
    background: var(--brand-red);
  }
  .brand-name {
    position: absolute; left: 44px; top: 60px;
    font-weight: 500; font-size: 29px; letter-spacing: -0.6px;
    color: var(--brand-red);
  }
  .header-block {
    position: absolute; top: 54px;
    font-size: 13.2px; line-height: 16px;
    color: var(--ink-soft);
    padding-left: 14px;
    border-left: 1px solid var(--rule);
  }
  .office { left: 350px; }
  .contact { left: 560px; }
  .contact li { list-style: none; display: flex; align-items: center; gap: 6px; }
  .contact svg { width: 10px; height: 10px; fill: var(--brand-red); flex: none; }
  .letter {
    position: absolute; left: 84px; top: 272px; width: 623px;
    font-size: 13px; line-height: 18.7px;
  }
  .letter .date { margin-bottom: 18.7px; }
  .letter .recipient { margin-bottom: 37px; }
  .letter .salutation { margin-bottom: 18.7px; }
  .letter .body p { text-align: justify; margin-bottom: 18.7px; }
  .letter .closing { margin-top: 46px; }
  .letter .signature {
    font-family: "Pinyon Script", cursive;
    font-size: 26px; line-height: 34px; margin-left: 4px; font-weight: 400;
  }
  .ghost-name { position: absolute; left: 0; bottom: 0; width: 792px; height: 90px; }
  .ghost-name text { font-family: "Roboto", Arial, sans-serif; font-weight: 300; fill: var(--ghost); }
</style>
</head>
<body>
<main class="letterhead">
  <div class="accent-bar"></div>
  <div class="brand-name">KelbrinStaffing</div>

  <address class="header-block office" style="font-style:normal">
    Central Houston Office<br>
    48 Larkmoor Plaza Suite 900<br>
    Houston, TX 77051
  </address>

  <ul class="header-block contact">
    <li><svg viewBox="0 0 10 10"><path d="M2 0.5 L3.8 2.6 L2.9 3.7 Q4 6 6.3 7.1 L7.4 6.2 L9.5 8 L8.3 9.5 Q2.5 9 0.5 1.7 Z"/></svg>(+1) 555-014-2287</li>
    <li><svg viewBox="0 0 10 10"><path d="M0.5 2 H9.5 V8 H0.5 Z M0.5 2 L5 5.5 L9.5 2" fill="none" stroke="#e31e24" stroke-width="1.2"/></svg>info@kelbrinstaffing.com</li>
    <li><svg viewBox="0 0 10 10"><circle cx="5" cy="5" r="4.4" fill="none" stroke="#e31e24" stroke-width="1.1"/><path d="M0.6 5 H9.4 M5 0.6 Q2.2 5 5 9.4 M5 0.6 Q7.8 5 5 9.4" fill="none" stroke="#e31e24" stroke-width="0.9"/></svg>www.kelbrinstaffing.com</li>
  </ul>

  <article class="letter">
    <p class="date">01 January 2050</p>
    <p class="recipient">Company (Pvt) Ltd.<br>PO Box 3355 Mainville St<br>Sample City Country 3355</p>
    <p class="salutation">Dear Daniel Ashcroft,</p>
    <div class="body">
      <p>Lorem ipsum dolor sit amet, consectetuer adipiscing elit, sed diam nonummy nibh euismod tincidunt ut laoreet dolore magna aliquam erat volutpat. Ut wisi enim ad minim veniam, quis nostrud exerci tation ullamcorper suscipit lobortis nisl ut aliquip ex ea commodo consequat. Duis dolore te feugait nulla facilisi. Nam liber tempor cum soluta nobis eleifend option congue nihil imperdiet doming id quod mazim placerat facer possim assum. Lorem ipsum dolor sit amet, consectetuer adipiscing elit, sed diam nonummy nibh euismod tincidunt ut laoreet dolore magna aliquam erat volutpat. Ut wisi enim ad minim veniam, quis nostrud exerci tation ullamcorper suscipit lobortis nisl ut aliquip ex ea commodo consequat.</p>
      <p>Consectetuer adipiscing elit, sed diam nonummy nibh euismod tincidunt ut laoreet dolore magna aliquam erat volutpat. Ut wisi enim ad minim veniam, quis nostrud exerci tation ullamcorper suscipit lobortis nisl ut aliquip ex ea commodo consequat. Consectetuer adipiscing elit, sed diam nonummy nibh euismod tincidunt ut laoreet dolore magna aliquam erat volutpat. Ut wisi enim ad minim veniam, quis nostrud exerci tation ullamcorper suscipit lobortis nisl ut aliquip ex ea commodo consequat.</p>
      <p>Consectetuer adipiscing elit, sed diam nonummy nibh euismod tincidunt ut laoreet dolore magna aliquam erat volutpat. Ut wisi enim ad minim veniam, quis nostrud exerci tation ullamcorper suscipit lobortis nisl ut aliquip ex ea commodo consequat. Consectetuer adipiscing elit, sed diam nonummy nibh euismod tincidunt ut laoreet dolore magna aliquam erat volutpat. Ut wisi enim ad minim veniam, quis nostrud exerci tation ullamcorper suscipit lobortis nisl ut aliquip ex ea commodo consequat.</p>
    </div>
    <p class="closing">Sincerely Yours</p>
    <p class="signature">Owen Hartley</p>
  </article>

  <svg class="ghost-name" viewBox="0 0 792 90" aria-hidden="true">
    <text x="0" y="90" font-size="108" textLength="792" lengthAdjust="spacingAndGlyphs">KelbrinStaffing</text>
  </svg>
</main>
</body>
</html>
```